Postcard Design

We are a small Jewelry store in Vermont and carry high end Estate Jewelry. We are trying to promote 3 rings we took in recently. I have attached pictures and would like to send text as well for each ring with pricing. We would like two images of each and colorful background but classy. I am also sending our logo, address and contact info which must go on the card. We would like the finish on the front to be glossy if possible. Please let me know what else may be needed to complete this project as quickly as possible. The text is as follows: 1. Platinum 3-stone Diamond ring with 4.61ct Round Brilliant center J VVS2 and two Round brilliant side Diamonds 2.72ctw I-J VVS2-VS1 NQB Certified and Value is $175,000.00 Special Price $125,000.00 2. 18k yellow gold and Platinum ring with 5.50ct Emerald in the center and 1.22ctw in trillion cut diamonds on the sides G-H SI1 Certified value $32,620.00 Special price $25,000.00 3. 18k white gold ring with gorgeous cushion cut Sapphire 5.40ct and .55ctw accent diamonds G-H SI1-2 Retail Value $18,000.00 Special price $12,500.00 Our contact information as follows: Our Logo which I atttached, address: 48 Larkfield Rd. Marrow Hill VT 05273 Phone: 802-639-4258

```html
<!DOCTYPE html>
<html lang="en">
<head>
<meta charset="utf-8">
<title>Ashby Estate &amp; Custom Jewelers — Postcard</title>
<link rel="stylesheet" href="https://fonts.googleapis.com/css2?family=EB+Garamond:ital,wght@0,400;0,600;1,400&display=swap">
<style>
  :root {
    --page: #e9e6e1;
    --card: #ffffff;
    --ink: #3a3a3a;
    --muted: #555555;
    --brand: #2f2f8c;
    --accent: #3c3ca8;
    --rule: #6a6ab8;
    --photo-dark: #141414;
  }
  * { box-sizing: border-box; margin: 0; padding: 0; }
  html, body { width: 1200px; height: 1109px; overflow: hidden; }
  body {
    background: var(--page);
    font-family: "EB Garamond", Georgia, serif;
    color: var(--ink);
    position: relative;
  }
  .postcard {
    position: absolute;
    width: 700px;
    height: 500px;
    background: var(--card);
    box-shadow: 0 4px 14px rgba(0,0,0,0.18);
  }

  /* front */
  .postcard--front { left: 100px; top: 40px; }
  .front-grid {
    display: grid;
    grid-template-columns: 1fr 1fr;
    grid-template-rows: 1fr 1fr;
    gap: 9px;
    width: 100%;
    height: 100%;
  }
  .photo { width: 100%; height: 100%; }
  .photo--diamond { background: radial-gradient(ellipse at 50% 45%, #8d8d8d 0%, #3a3a3a 35%, var(--photo-dark) 75%); }
  .photo--sapphire { background: radial-gradient(ellipse at 50% 40%, #3b3fa0 0%, #252a5a 28%, #1c1c1c 60%, var(--photo-dark) 90%); }
  .photo--emerald { background: radial-gradient(ellipse at 50% 50%, #1b8a4c 0%, #5b5a2a 30%, #222 60%, var(--photo-dark) 90%); }
  .front-brand {
    display: flex;
    flex-direction: column;
    align-items: center;
    justify-content: center;
    text-align: center;
  }
  .wordmark {
    color: var(--brand);
    font-weight: 400;
    font-size: 40px;
    letter-spacing: 3px;
    line-height: 1;
    padding: 0 4px 6px;
    border-bottom: 1px solid var(--brand);
  }
  .wordmark-sub {
    color: var(--brand);
    font-weight: 400;
    font-size: 22px;
    margin-top: 8px;
  }
  .front-location {
    margin-top: 22px;
    font-size: 16px;
    letter-spacing: 2px;
    color: var(--muted);
  }

  /* back */
  .postcard--back { left: 420px; top: 569px; padding: 36px 40px; }
  .back-header { display: flex; align-items: flex-start; gap: 22px; }
  .back-logo { color: var(--brand); line-height: 1; }
  .back-logo .name { font-size: 22px; letter-spacing: 2px; padding-bottom: 3px; border-bottom: 1px solid var(--brand); }
  .back-logo .sub { font-size: 12px; margin-top: 4px; }
  .back-contact { font-size: 12px; letter-spacing: 1px; line-height: 1.45; color: var(--muted); padding-top: 4px; }
  .thumbs { display: flex; gap: 14px; margin-top: 14px; }
  .thumb { width: 102px; height: 62px; position: relative; }
  .thumb-num { position: absolute; left: 5px; bottom: 3px; font-size: 10px; color: #ddd; }
  .stamp {
    position: absolute; right: 38px; top: 92px;
    width: 84px; height: 100px;
    border: 1px solid #999;
    display: flex; align-items: center; justify-content: center;
    text-align: center; font-size: 11px; line-height: 1.3; color: var(--muted); letter-spacing: 0.5px;
  }
  .ring-list { list-style: none; margin-top: 24px; width: 330px; }
  .ring-item { font-size: 12px; line-height: 1.25; margin-bottom: 14px; }
  .ring-num { font-weight: 600; color: var(--accent); }
  .ring-price { margin-top: 2px; }
  .ring-value { font-weight: 600; font-style: italic; }
  .ring-special { font-style: italic; color: var(--accent); margin-left: 8px; }
  .address-lines { position: absolute; right: 40px; top: 250px; width: 240px; }
  .address-line { height: 36px; border-bottom: 1px solid var(--rule); }
</style>
</head>
<body>

<section class="postcard postcard--front">
  <div class="front-grid">
    <div class="photo photo--diamond" role="img" aria-label="Platinum three-stone diamond ring on a dark reflective background"></div>
    <div class="photo photo--sapphire" role="img" aria-label="White gold ring with cushion cut sapphire and diamond halo on a dark background"></div>
    <div class="photo photo--emerald" role="img" aria-label="Yellow gold and platinum emerald ring with trillion diamonds on a dark background"></div>
    <div class="front-brand">
      <div class="wordmark">ASHBY</div>
      <div class="wordmark-sub">Estate &amp; Custom Jewelers</div>
      <div class="front-location">Marrow Hill, Vermont</div>
    </div>
  </div>
</section>

<section class="postcard postcard--back">
  <header class="back-header">
    <div class="back-logo">
      <div class="name">ASHBY</div>
      <div class="sub">Estate &amp; Custom Jewelers</div>
    </div>
    <div class="back-contact">
      48 Larkfield Rd. Marrow Hill, VT 05273<br>
      Phone: 802-639-4258
    </div>
  </header>

  <div class="thumbs">
    <div class="thumb photo--diamond" role="img" aria-label="Diamond ring, second view"><span class="thumb-num">1.</span></div>
    <div class="thumb photo--emerald" role="img" aria-label="Emerald ring, second view"><span class="thumb-num">2.</span></div>
    <div class="thumb photo--sapphire" role="img" aria-label="Sapphire ring, second view"><span class="thumb-num">3.</span></div>
  </div>

  <div class="stamp">PLACE<br>STAMP<br>HERE</div>

  <ol class="ring-list">
    <li class="ring-item">
      <span class="ring-num">1.</span> Platinum 3-stone Diamond ring with 4.61ct round brilliant center J VVS2 and two round brilliant side Diamonds. 2.72ctw I-J VVS2-VS1 NQB Certified.
      <div class="ring-price"><span class="ring-value">Value: $175,000.00</span><span class="ring-special">Special Price $125,000.00</span></div>
    </li>
    <li class="ring-item">
      <span class="ring-num">2.</span> 18k yellow Gold and Platinum ring with 5.50ct Emerald in the center and 1.22ctw in trillion cut diamonds on the sides. G-H SI1 Certified.
      <div class="ring-price"><span class="ring-value">Value: $32,620.00</span><span class="ring-special">Special Price $25,000.00</span></div>
    </li>
    <li class="ring-item">
      <span class="ring-num">3.</span> 18k White Gold ring with gorgeous cushion cut Sapphire 5.40ct and .55ctw accent diamonds. G-H SI1-2 Certified.
      <div class="ring-price"><span class="ring-value">Value: $18,000.00</span><span class="ring-special">Special Price $12,500.00</span></div>
    </li>
  </ol>

  <div class="address-lines">
    <div class="address-line"></div>
    <div class="address-line"></div>
    <div class="address-line"></div>
    <div class="address-line"></div>
  </div>
</section>

</body>
</html>
```